HK-Steuerberatung WordPress Site fully implemented (tax advisor)

Hello!
I need a little Wordpress Site for my newly founded Tax-Advisor Company.
I am a one-man Office advising in the area of Crypto-Currency.
PLEASE only provide a Design, if you can also Implement a WP-Site afterwards on an existing Webspace.

Please find the Content and Website-Description in the attached Document

Language for the Website is German (for now)

Target Market(s)

Tax-Advisory (specialized in Crypto Currency)

Coding

Coded - Design and coding required

Number of Pages Required

5+ page

Font styles to use
Sans Serif

Requirements
Must have
• Wordpress Implementation afterwards - Details according to attached Project Information Document

```html
<!DOCTYPE html>
<html lang="de">
<head>
<meta charset="utf-8">
<title>HK-Steuerberatung</title>
<link href="https://fonts.googleapis.com/css2?family=Inter:wght@300;400;500;600;700&display=swap" rel="stylesheet">
<style>
:root{--navy:#1a2a41;--grey:#a9a9a9;--light:#e8e9ed;--bg:#f6f6f7;--text:#5b6270;--white:#fff}
*{margin:0;padding:0;box-sizing:border-box}
html,body{width:1200px;height:3600px;overflow:hidden}
body{position:relative;background:var(--white);font-family:"Inter",sans-serif;color:var(--text)}
.abs{position:absolute}
.topbar{left:0;top:0;width:1200px;height:34px;font-size:10px}
.topbar .follow{left:161px;top:11px;color:var(--navy)}
.topbar .follow i{display:inline-block;width:9px;height:9px;border-radius:50%;background:var(--navy);margin-left:6px;vertical-align:-1px}
.topbar .dark{left:599px;top:0;width:601px;height:34px;background:var(--navy);color:#fff;display:flex;align-items:center;justify-content:center;gap:26px;padding-left:40px}
.topbar .dark span{display:flex;align-items:center;gap:7px}
.header{top:34px;left:0;width:1200px;height:88px;background:#fff}
.brand{font-weight:700;color:var(--navy);display:flex;align-items:center;gap:8px;letter-spacing:.02em}
.brand b{display:block;width:22px;height:22px;background:var(--navy)}
.header .brand{left:161px;top:31px;font-size:15px}
.nav{left:614px;top:38px;display:flex;gap:42px;font-size:11px;color:#6d7380;letter-spacing:.02em}
.hero{top:122px;left:0;width:1200px;height:700px;background:var(--bg)}
.hero h1{top:195px;width:1200px;text-align:center;color:var(--navy);font-weight:300;font-size:40px;line-height:50px}
.hero h1 strong{display:block;font-weight:700;font-size:40px;line-height:56px}
.hero p{top:320px;width:1200px;text-align:center;font-size:12.5px;line-height:22px}
.more{font-size:10.5px;font-weight:600;color:var(--navy);display:flex;align-items:center;gap:8px;letter-spacing:.02em}
.hero .more{top:400px;left:0;width:1200px;justify-content:center}
.sec-title{font-size:32px;font-weight:700;color:var(--navy);display:flex;align-items:center;gap:18px;letter-spacing:.01em}
.sec-title b{display:block;width:24px;height:24px;background:var(--navy)}
.intro{font-size:11.5px;line-height:18px}
.services{left:161px;top:1035px;display:grid;grid-template-columns:312px 343px 300px;row-gap:26px}
.svc{display:flex;gap:14px;font-size:10px;line-height:17px}
.svc svg{flex:none;margin-top:1px}
.body{font-size:11.5px;line-height:18px}
.body strong{color:var(--navy);font-weight:500}
.tabs{left:161px;top:2080px;display:flex;gap:42px;font-size:10px;color:var(--grey)}
.tabs .on{color:var(--navy);font-weight:600}
.photo{left:668px;top:1966px;width:373px;height:488px;border:1px solid var(--light);background:#fff}
.photo .img{left:0;top:0;width:373px;height:392px;background:linear-gradient(180deg,#f4f4f5 0%,#dcdde1 60%,#2a3550 100%)}
.photo .name{left:0;top:392px;width:373px;height:96px;background:var(--navy);color:#fff;font-size:17px;font-weight:600;display:flex;align-items:center;justify-content:center;gap:12px}
.photo .name i{width:26px;height:26px;border-radius:50%;background:#6c7588}
.rule{left:161px;top:2526px;width:880px;height:1px;background:var(--light)}
.contacts{top:2688px;left:0;width:1200px;display:flex;justify-content:center;gap:60px;font-size:11.5px;color:var(--navy)}
.contacts span{display:flex;align-items:center;gap:16px}
.contacts em{width:40px;height:40px;border-radius:50%;background:#fff;box-shadow:0 4px 14px rgba(26,42,65,.12);display:flex;align-items:center;justify-content:center}
.field label{display:block;font-size:9.5px;margin-bottom:7px}
.field div{border:1px solid #d3d6dc;height:44px}
.btn{left:528px;top:3135px;width:142px;height:42px;background:var(--navy);color:#fff;font-size:9.5px;font-weight:700;display:flex;align-items:center;justify-content:center;letter-spacing:.04em}
.footer{color:#fff}
.footer h4{font-size:12px;font-weight:600;margin-bottom:10px}
.footer p{font-size:10px;line-height:18px;color:#8d96a8}
</style>
</head>
<body>

<div class="abs topbar">
  <div class="abs follow">Follow me on ProNetz<i></i></div>
  <div class="abs dark">
    <span><svg width="11" height="11" viewBox="0 0 24 24" fill="#fff"><path d="M6.6 10.8a15 15 0 0 0 6.6 6.6l2.2-2.2a1 1 0 0 1 1-.25 11.4 11.4 0 0 0 3.6.57 1 1 0 0 1 1 1V20a1 1 0 0 1-1 1A17 17 0 0 1 3 4a1 1 0 0 1 1-1h3.5a1 1 0 0 1 1 1c0 1.250.2 2.450.57 3.57a1 1 0 0 1-.25 1z"/></svg>+43 512 400 217</span>
    <span><svg width="12" height="10" viewBox="0 0 24 18" fill="#fff"><path d="M0 0h24v18H0zM2 2v1l10 7 10-7V2z"/></svg>office@hk-steuer.example</span>
  </div>
</div>

<header class="abs header">
  <div class="abs brand"><b></b>HK STEUERBERATUNG</div>
  <nav class="abs nav"><span>HOME</span><span>LEISTUNGEN</span><span>ÜBER MICH</span><span>KONTAKT</span><span>IMPRESSUM</span></nav>
</header>

<section class="abs hero">
  <h1 class="abs">Willkommen bei<strong>HK-STEUERBERATUNG</strong></h1>
  <p class="abs">Ihrem Spezialisten bei allen steuerlichen Themen rund um<br>Einkünfte &amp; Vermögen aus Krypto-Assets.</p>
  <div class="abs more"><svg width="14" height="8" viewBox="0 0 14 8"><path d="M0 4h12M9 1l3 3-3 3" stroke="#1a2a41" fill="none" stroke-width="1.3"/></svg>WEITER ZU UNSEREN LEISTUNGEN</div>
</section>

<svg class="abs" style="left:0;top:0" width="1200" height="3600" aria-hidden="true">
  <polygon points="0,777 1200,700 1200,900 0,900" fill="#fff"/>
  <polygon points="830,777 1200,725 1200,900" fill="#e8e9ed"/>
  <polygon points="0,1248 0,1372 350,1352" fill="#e8e9ed"/>
  <polygon points="0,1440 1200,1365 1200,1888 0,1888" fill="#f6f6f7"/>
  <polygon points="0,3251 1200,3356 1200,3600 0,3600" fill="#1a2a41"/>
  <polygon points="880,3330 1200,3290 1200,3356" fill="#e8e9ed"/>
</svg>

<h2 class="abs sec-title" style="left:161px;top:858px"><b></b>LEISTUNGEN</h2>
<p class="abs intro" style="left:161px;top:931px;width:565px">Ich biete in meiner Kanzlei ausschließlich Spezialberatung rund um die komplexen und vielseitigen Themen im Krypto-Bereich sowie deren Besteuerung, bzw. der Besteuerung und steuerlichen Optimierung von anderen passiven Einkommensmodellen an:</p>

<div class="abs services">
  <div class="svc"><svg width="20" height="20" viewBox="0 0 20 20"><circle cx="10" cy="10" r="9" fill="none" stroke="#1a2a41" stroke-width="1.2"/><path d="M6 10l3 3 5-6" fill="none" stroke="#1a2a41" stroke-width="1.2"/></svg><span>Steueroptimales Besitzen von<br>KryptoAssets auf in- und<br>ausländischen Börsen</span></div>
  <div class="svc"><svg width="20" height="20" viewBox="0 0 20 20"><circle cx="10" cy="10" r="9" fill="none" stroke="#1a2a41" stroke-width="1.2"/><path d="M6 10l3 3 5-6" fill="none" stroke="#1a2a41" stroke-width="1.2"/></svg><span>Hilfestellung bei der Dokumentation<br>der Einkünfte (Verwendung von<br>Tax-Tools und Aufbereitung der</span></div>
  <div class="svc"><svg width="20" height="20" viewBox="0 0 20 20"><circle cx="10" cy="10" r="9" fill="none" stroke="#1a2a41" stroke-width="1.2"/><path d="M6 10l3 3 5-6" fill="none" stroke="#1a2a41" stroke-width="1.2"/></svg><span>Finanzstrafrechtliche Offenlegung<br>und Aufarbeitung bei Einkünften<br>die nicht ordnungsgemäß erklärt</span></div>
  <div class="svc"><svg width="20" height="20" viewBox="0 0 20 20"><circle cx="10" cy="10" r="9" fill="none" stroke="#1a2a41" stroke-width="1.2"/><path d="M6 10l3 3 5-6" fill="none" stroke="#1a2a41" stroke-width="1.2"/></svg><span>Beratung rund um das Thema<br>Wegzug, Wohnsitzverlegung und<br>in-/ausländische Gesellschaften</span></div>
  <div class="svc"><svg width="20" height="20" viewBox="0 0 20 20"><circle cx="10" cy="10" r="9" fill="none" stroke="#1a2a41" stroke-width="1.2"/><path d="M6 10l3 3 5-6" fill="none" stroke="#1a2a41" stroke-width="1.2"/></svg><span>Hilfe bei der korrekten Erklärung der<br>Crypto-Einkünfte und Erstellung der<br>Steuererklärungen</span></div>
  <div class="svc"><svg width="20" height="20" viewBox="0 0 20 20"><circle cx="10" cy="10" r="9" fill="none" stroke="#1a2a41" stroke-width="1.2"/><path d="M6 10l3 3 5-6" fill="none" stroke="#1a2a41" stroke-width="1.2"/></svg><span>Beratung bei der Unterscheidung<br>und Besteuerung der diversen<br>Einkunftsmöglichkeiten (Trading,<br>Staking, Lending, Mining, Nodes,</span></div>
</div>

<h2 class="abs sec-title" style="left:161px;top:1510px"><b></b>KOLLEGENDIENST</h2>
<p class="abs intro" style="left:329px;top:1583px;width:440px">Ihr Fokus liegt in der traditionellen Steuerberatung und Sie haben<br>keine Zeit sich das hochkomplexe Spezialthema Kryptowährungen etc.</p>
<p class="abs intro" style="left:557px;top:1646px;width:460px">Um Ihre Klienten dennoch weiterhin vollumfänglich beraten zu<br>können, biete ich Ihnen gerne mein Know-How und die gesamte<br>Leistungspalette an um Ihre Kunden ganz nach Ihrem Wunsch<br>entweder direkt oder diskret im Hintergrund bei sämtlichen Themen<br>rund um Krypto mit steuerlicher Expertise dazu zu unterstützen.</p>
<div class="abs more" style="left:762px;top:1797px"><svg width="14" height="8" viewBox="0 0 14 8"><path d="M0 4h12M9 1l3 3-3 3" stroke="#1a2a41" fill="none" stroke-width="1.3"/></svg>NEHMEN SIE GERNE KONTAKT MIT MIR AUF!</div>

<h2 class="abs sec-title" style="left:161px;top:1996px"><b></b>ÜBER MICH</h2>
<div class="abs tabs"><span class="on">ÜBER MICH</span><span>AUSBILDUNG</span><span>BERUFLICHER WERDEGANG</span></div>
<p class="abs body" style="left:161px;top:2131px;width:402px">Mag. <strong>Markus Lehner</strong> Ich blicke auf eine sehr umfassende Ausbildung und langjährige Berufserfahrung in der IT Branche zurück. Nach Abschluss des Wirtschaftsstudiums habe ich den klassischen Weg der Steuerberaterausbildung absolviert und bin in diesem Bereich seit über <strong>13 Jahren beratend tätig.</strong></p>
<p class="abs body" style="left:161px;top:2240px;width:402px">Durch die Kombination meines umfassenden Wissens in der IT und der Wirtschaft habe ich schon immer gerne Unternehmen mit besonderes technischen oder digitalen Geschäftsmodellen beraten. Seit mehreren Jahren bin ich privat an der Blockchain-technologie und dem Krypto-Universum interessiert und bereits seit dem <strong>Jahre 2017</strong> ist dieses Thema auch Teil meiner fixen Beratungsfelder in der Steuerberatung.</p>

<div class="abs photo">
  <div class="abs img" role="img" aria-label="Porträtfoto des Steuerberaters im dunklen Anzug"></div>
  <div class="abs name">Markus Lehner<i></i></div>
</div>

<div class="abs rule"></div>

<h2 class="abs sec-title" style="left:0;width:1200px;justify-content:center;top:2602px"><b></b>KONTAKT</h2>
<div class="abs contacts">
  <span><em><svg width="16" height="16" viewBox="0 0 24 24" fill="none" stroke="#a9a9a9" stroke-width="1.5"><path d="M6.6 10.8a15 15 0 0 0 6.6 6.6l2.2-2.2a1 1 0 0 1 1-.25 11.4 11.4 0 0 0 3.6.57 1 1 0 0 1 1 1V20a1 1 0 0 1-1 1A17 17 0 0 1 3 4a1 1 0 0 1 1-1h3.5a1 1 0 0 1 1 1c0 1.250.2 2.450.57 3.57a1 1 0 0 1-.25 1z"/></svg></em>office@hk-steuer.example</span>
  <span><em><svg width="16" height="12" viewBox="0 0 24 18" fill="none" stroke="#a9a9a9" stroke-width="1.5"><rect x="1" y="1" width="22" height="16"/><path d="M1 1l11 8 11-8"/></svg></em>+43 512 400 217</span>
</div>

<div class="abs field" style="left:233px;top:2783px;width:356px"><label>First Name</label><div></div></div>
<div class="abs field" style="left:604px;top:2783px;width:356px"><label>Second Name</label><div></div></div>
<div class="abs field" style="left:233px;top:2867px;width:234px"><label>Email</label><div></div></div>
<div class="abs field" style="left:483px;top:2867px;width:231px"><label>Phone</label><div></div></div>
<div class="abs field" style="left:730px;top:2867px;width:230px"><label>Subject</label><div></div></div>
<div class="abs field" style="left:233px;top:2950px;width:727px"><label>Message</label><div style="height:140px"></div></div>
<div class="abs btn">SUBMIT MESSAGE</div>

<div class="abs footer" style="left:161px;top:3418px">
  <div class="brand" style="color:#fff;font-size:14px"><b style="background:#fff"></b>HK STEUERBERATUNG</div>
  <p style="margin-top:24px;width:220px">Ihrem Spezialisten bei allen steuerlichen Themen rund um Einkünfte &amp; Vermögen aus Krypto-Assets.</p>
</div>
<div class="abs footer" style="left:685px;top:3412px"><h4>Email</h4><p>office@hk-steuer.example</p></div>
<div class="abs footer" style="left:953px;top:3412px"><h4>Phone</h4><p>+43 512 400 217</p></div>
<div class="abs footer" style="left:685px;top:3517px"><h4>Quick Links</h4><p>Leistungen<br>Über mich</p></div>
<div class="abs footer" style="left:953px;top:3517px"><h4>Privacy</h4><p>Impressum</p></div>

</body>
</html>
```